Business card - house cleaning company

We want friendly high end business card highlighting our services . NO LOGOs on back of card please.. no vertical cards NO DOUBLE BROOMS

2 owners of the company: Corinne Halvey & Joel Brandt

Included phone number: (555)318-2047

Email: brightlanetidy@mailnest.example

Website: www.brightlanetidy.example

Bonded & Insured

Alder Ridge, CO 80000

Slogan maybe: Bringing a brighter shine to every corner of home

We want elegant high end card for house cleaning service. Maybe 2 sided if needed. Can it have bullet points of some services we offer

Residential Home Cleaning
Vacation Rental Cleaning
Commercial Cleaning
Carpet Cleaning
Window Cleaning
Property Management
Property Inspections
Property Maintenance
Trash Removal
Concierge Services

Highlight service on back of card. If we can do a one sided card with all this that’s great as well. Not cartoony.

Our logo attached and a design somone I had Perrin but they put very little time in. Not Unique enough. If you can do a custom design with a feminine touch that be great.

You will be eliminated for not reading the brief. NO DOUBLE LOGOS NO DOUBLE BROOMS. PLEASE BE CREATIVE. IF POST SAME LOGO WITH SMAL CHANGES RHEY WILL BE ELIMINATED. BE CREATIVE.

Thank you everyone for your designs. please only use the logo 1 time. and would love to see some that dont look all the same. We appreciate your time.

Target Market(s)

Residential and vacation rental home cleaning maid service

Industry/Entity Type

House cleaning maid services

Contact Information for Business Card

For business card use logo. black and green one provided. others for example. I wil try find some example.. We want friendly high end look. 2 owners of the company: Corinne Halvey & Joel Brandt Included phone number: (555)318-2047 Email: brightlanetidy@mailnest.example Website: www.brightlanetidy.example Bonded & Insured Estes Park, CO Slogan maybe: Bringing a brighter shine to every corner of home or Quality Service Guaranteed We want elegant high end card for house cleaning service. Maybe 2 sided if needed. Can it have bullet points of some services we offer Residential Home Cleaning Vacation Rental Cleaning Commercial Cleaning Carpet Cleaning Window Cleaning Property Management Property Inspections Property Maintenance Trash Removal Concierge Services

Requirements
Must have
• For business card use logo . Creativity. black and green one provided. We want friendly high end look. 2 owners of the company: Corinne Halvey & Joel Brandt Included phone number: (555)318-2047 Email: brightlanetidy@mailnest.example Website: www.brightlanetidy.example Licensed Bonded & Insured Estes Park, CO Slogan maybe: Bringing a brighter shine to every corner of home or Quality Service Guaranteed We want elegant high end card for house cleaning service. Maybe 2 sided if needed. Can it have bullet points of some services we offer Residential Home Cleaning Vacation Rental Cleaning Commercial Cleaning Carpet Cleaning Window Cleaning Property Management Property Inspections Property Maintenance Trash Removal Concierge Services .. creatitivty a plus. whimsical. we like stars..
Nice to have
• we want much better than the example of biz card provided as example. logo has colors that are in our website palette as well. We are open to ideas for the business card design. Will pay tip to best work. PLEASE USE COMPLIMENTING COLORS. . WE LIKE BLACK AND WHITE, stars
Should not have
• NO DOUBLE LOGOS. READ READ. READ. YOU WILL BE ELIMINATED no double logos or double brooms same side of card. I want didfrent examples. please don't make all your submission look the same

```html
<!DOCTYPE html>
<html lang="en">
<head>
<meta charset="utf-8">
<title>Bright Lane Tidy – Business Card</title>
<link rel="stylesheet" href="https://fonts.googleapis.com/css2?family=Cinzel:wght@500;600&family=Gilda+Display&family=Satisfy&display=swap">
<style>
  :root {
    --page: #202123;
    --card-black: #000000;
    --card-charcoal: #2a2a2b;
    --strip-grey: #111111;
    --green: #6a9a45;
    --green-dark: #4f7a3a;
    --band-end: #151b17;
    --white: #ffffff;
    --rule: #cfcfcf;
  }
  * { margin: 0; padding: 0; box-sizing: border-box; }
  html, body { width: 1200px; height: 800px; overflow: hidden; background: var(--page); }
  .card {
    position: absolute; left: 0; top: 40px; width: 1200px; height: 720px;
    background:
      radial-gradient(ellipse 520px 230px at 50% 0%, rgba(150,150,150,.75), rgba(60,60,60,.2) 70%, transparent 100%),
      linear-gradient(180deg, var(--card-charcoal) 0%, #141414 55%, var(--card-black) 80%);
    overflow: hidden; color: var(--white);
  }
  .brand {
    position: absolute; top: 140px; left: 0; width: 100%;
    display: flex; justify-content: center; align-items: center; gap: 16px;
  }
  .brand-dot { width: 22px; height: 22px; border-radius: 50%; background: var(--green); }
  .brand-name {
    font-family: "Gilda Display", serif; font-size: 60px; line-height: 1; color: var(--white);
  }
  .tagline {
    position: absolute; left: 363px; width: 475px; top: 269px; height: 58px;
    border-top: 1px solid var(--rule); border-bottom: 1px solid var(--rule);
    display: flex; align-items: center; justify-content: center;
    font-family: "Satisfy", cursive; font-size: 22px; color: var(--green); white-space: nowrap;
  }
  .owners {
    position: absolute; top: 340px; left: 0; width: 100%;
    display: flex; justify-content: center; align-items: center;
    font-family: "Gilda Display", serif; font-size: 22px;
  }
  .owners .phone { font-size: 25px; }
  .icon-circle {
    width: 34px; height: 34px; border-radius: 50%; background: var(--green);
    display: inline-flex; align-items: center; justify-content: center; margin: 0 14px 0 16px;
  }
  .services {
    position: absolute; top: 418px; left: 0; width: 100%; height: 96px;
    background: linear-gradient(90deg, var(--green-dark) 0%, #3e5c35 45%, var(--band-end) 100%);
    display: flex; flex-direction: column; justify-content: center; gap: 14px;
    font-family: "Cinzel", serif; font-weight: 600; font-size: 13.5px; text-align: center;
  }
  .services p { white-space: nowrap; }
  .services .sep { margin: 0 8px; }
  .gap-strip { position: absolute; top: 514px; left: 0; width: 100%; height: 24px; background: var(--strip-grey); }
  .contact {
    position: absolute; top: 538px; left: 0; width: 100%; height: 54px; background: var(--card-black);
    display: flex; justify-content: center; align-items: center;
    font-family: "Gilda Display", serif; font-size: 17px;
  }
  .contact .icon-circle { margin: 0 8px 0 0; }
  .contact .divider { margin: 0 26px; }
  .credentials {
    position: absolute; top: 592px; left: 0; width: 100%; height: 48px; background: var(--strip-grey);
    display: flex; justify-content: center; align-items: center; gap: 12px;
    font-family: "Cinzel", serif; font-weight: 500; font-size: 20px; letter-spacing: .5px;
    text-transform: uppercase;
  }
</style>
</head>
<body>
  <section class="card">
    <div class="brand">
      <span class="brand-dot"></span>
      <span class="brand-name">Bright Lane Tidy</span>
    </div>

    <p class="tagline">Bringing a brighter shine to every corner of home</p>

    <div class="owners">
      <span class="names">Corinne Halvey &amp; Joel Brandt</span>
      <span class="icon-circle">
        <svg width="14" height="20" viewBox="0 0 14 20"><rect x="1.5" y="1" width="11" height="18" rx="2" fill="none" stroke="#fff" stroke-width="1.6"/><circle cx="7" cy="16" r="1" fill="#fff"/></svg>
      </span>
      <span class="phone">(555)318-2047</span>
    </div>

    <div class="services">
      <p>Residential Home Cleaning<span class="sep">|</span>Vacation Rental Cleaning<span class="sep">|</span>Commercial Cleaning<span class="sep">|</span>Carpet Cleaning<span class="sep">|</span>Window Cleaning</p>
      <p>Property Management<span class="sep">|</span>Property Inspections<span class="sep">|</span>Property Maintenance<span class="sep">|</span>Trash Removal<span class="sep">|</span>Concierge Services</p>
    </div>

    <div class="gap-strip"></div>

    <div class="contact">
      <span class="icon-circle">
        <svg width="20" height="20" viewBox="0 0 20 20"><circle cx="10" cy="10" r="8" fill="none" stroke="#fff" stroke-width="1.4"/><ellipse cx="10" cy="10" rx="3.5" ry="8" fill="none" stroke="#fff" stroke-width="1.2"/><line x1="2" y1="10" x2="18" y2="10" stroke="#fff" stroke-width="1.2"/></svg>
      </span>
      <span>Website : www.brightlanetidy.example</span>
      <span class="divider">|</span>
      <span class="icon-circle">
        <svg width="20" height="16" viewBox="0 0 20 16"><rect x="1.5" y="2" width="17" height="12" rx="1.5" fill="none" stroke="#fff" stroke-width="1.4"/><polyline points="2,3 10,9.5 18,3" fill="none" stroke="#fff" stroke-width="1.4"/></svg>
      </span>
      <span>brightlanetidy@mailnest.example</span>
    </div>

    <div class="credentials">
      <svg width="16" height="20" viewBox="0 0 16 20"><path d="M8 0C3.6 0 0 3.4 0 7.6 0 13 8 20 8 20s8-7 8-12.4C16 3.4 12.4 0 8 0z" fill="#fff"/><circle cx="8" cy="7.5" r="3" fill="#111"/></svg>
      <span>Bonded &amp; Insured&nbsp;&nbsp;|&nbsp;&nbsp;Alder Ridge, CO 80000</span>
    </div>
  </section>
</body>
</html>
```